Moulding supply company needs a Door Hanger Design

Door Hanger Design Request from Ledge Craft
www. ledgecrafts.example
We are moulding factory outlet in Toronto. Provide high quality moulding materials with competitive price like crown mouldings, casings, wainscoting, flatstocks, baseboards. We also provide professional installation for our clients. This door hanger will help the home owner easily find a local factory supplier with providing the materials as well as installation.

Detail request for design:
Size: 4”x11”, vertical
Shape: Rectangle

Content:
Front
1. Logo, see attachment(Use the left one, horizontal one)
2. Moulding factory outlet direct sale
3. Supply high quality Crown mouldings, baseboards, casings and wainscotings with competitive price
4. Installation & delivery
#2 content is the most important content, should be bold and readable
#3 can be smaller font compare to #2

Address: 47 North Willow Vale Rd, Richmond Hill, ON L4B 3K9
Telephone: 416 555 0143
416 555 0187
Email: info@ledgecrafts.example

Back
Slogan: Convert plain room into designer’s interiors

Telephone: 416 555 0143
416 555 0187
Email: info@ledgecrafts.example

Images:
Front
1. Display our productions for crown mouldings, baseboards, casings and wainscotings, refer to our website www.ledgecrafts.example. (The winner finally we will provide the high resolution images, low resolution please copy from our website so far)
Back
2. Display 4-6 nice images for 1. wainscoting walls 2. feature walls, 3. waffle ceiling like attached below. BUT PLEASE DON'T USE THE IMAGES PROVIDED, THIS IS ONLY A SAMPLE. Please use high resolution images for printing. ALSO PLEASE DON'T LIMIT YOUR CREATIVITY TO USE 4 SQUARES LIKE BELOW IMAGES. Please provide more ideas

Note:
1. Please do the bleeding for final printing production
2. Images have to be high resolution for ready to print
3. Style need to be fresh, clean, easy to read, modern and magazine style
4. Information has to be readable, easy to find, front and back both need to display company address, telephone, email, you can use icon or abbreviation to do these information.

Thanks,
Ledge Crafts

```html
<!DOCTYPE html>
<html lang="en">
<head>
<meta charset="utf-8">
<title>Ledge Crafts Door Hangers</title>
<link href="https://fonts.googleapis.com/css2?family=Oswald:wght@500&family=Montserrat:wght@300;400;500;600&family=Lato:wght@400&display=swap" rel="stylesheet">
<style>
  :root{
    --bg:#2c2c2c;
    --orange:#f0532a;
    --blue:#2a4f9f;
    --ink:#4a5560;
    --text:#5a5a5a;
    --dark:#222;
    --paper:#ffffff;
    --photo-a:#8e9aa0;
    --photo-b:#4f6a5e;
  }
  *{margin:0;padding:0;box-sizing:border-box}
  html,body{width:1200px;height:812px;overflow:hidden;background:var(--bg)}
  .canvas{position:relative;width:1200px;height:812px}
  .hanger{position:absolute;top:66px;width:248px;height:679px;background:var(--paper);overflow:hidden;font-family:'Montserrat',sans-serif}
  .hanger--front{left:327px;border-bottom:3px solid var(--orange)}
  .hanger--back{left:625px;border-top:3px solid var(--blue);border-bottom:3px solid var(--blue)}
  .hanger svg.top{position:absolute;left:0;top:0}
  .brand{position:absolute;left:0;width:100%;text-align:center}
  .brand__name{display:inline-flex;align-items:center;gap:6px;font-weight:500;font-size:17px;letter-spacing:1.5px;color:var(--ink)}
  .brand__mark{width:12px;height:12px;background:var(--orange)}
  .brand__tag{display:block;font-size:5.5px;letter-spacing:1.6px;color:var(--ink);margin-top:2px;padding-left:30px}
  .headline{position:absolute;top:322px;left:0;width:100%;text-align:center;font-family:'Oswald',sans-serif;font-weight:500;font-size:28px;line-height:31px;color:var(--orange);letter-spacing:.3px}
  .divider{position:absolute;top:387px;left:79px;width:90px;height:2px;background:var(--dark)}
  .intro{position:absolute;top:396px;left:20px;width:208px;text-align:center;font-weight:300;font-size:9.6px;line-height:11.4px;color:var(--text)}
  .service{position:absolute;top:434px;left:0;width:100%;height:34px;background:var(--blue);border-top:2px solid var(--orange);border-bottom:2px solid var(--orange);color:#fff;font-weight:600;font-size:14px;letter-spacing:.5px;text-align:center;line-height:30px}
  .collage{position:absolute;top:470px;left:0;width:248px;height:160px;background:linear-gradient(135deg,#4a4240 0%,#8a7a6a 45%,#e9e6df 75%,#c79a63 100%)}
  .contact{position:absolute;top:632px;left:0;width:100%;text-align:center;font-family:'Lato',sans-serif;font-size:8px;line-height:12.6px;color:var(--dark)}
  .slogan{position:absolute;top:344px;left:0;width:100%;text-align:center;font-weight:400;font-size:14px;line-height:17px;color:var(--orange)}
  .swatch{position:absolute;width:106px;height:106px;border-radius:50%;border:4px solid var(--blue)}
  .swatch--orange{border-color:var(--orange)}
  .swatch--baseboard{left:17px;top:387px;background:linear-gradient(120deg,#e6dcc4,#b89a6c)}
  .swatch--crown{left:125px;top:387px;background:linear-gradient(135deg,#1e1e1e 35%,#eeeeee 60%)}
  .swatch--wainscot{left:17px;top:495px;background:linear-gradient(135deg,#c9bdb3,#a99485)}
  .swatch--feature{left:125px;top:495px;background:linear-gradient(135deg,#3e3834,#6a625c)}
</style>
</head>
<body>
<main class="canvas">

  <section class="hanger hanger--front">
    <svg class="top" width="248" height="270" viewBox="0 0 248 270">
      <defs>
        <linearGradient id="factoryFront" x1="0" y1="0" x2="0" y2="1">
          <stop offset="0" stop-color="#b9c0c2"/>
          <stop offset=".55" stop-color="#7d8a8c"/>
          <stop offset="1" stop-color="#3f7562"/>
        </linearGradient>
      </defs>
      <path d="M0 0H248V236H138L124 255H0Z" fill="url(#factoryFront)" role="img" aria-label="Photo of a moulding factory floor"/>
      <path d="M0 258H126L140 240H248" fill="none" stroke="var(--orange)" stroke-width="5"/>
      <rect x="0" y="69" width="110" height="24" fill="var(--bg)"/>
      <circle cx="126" cy="80" r="51" fill="var(--bg)"/>
    </svg>
    <div class="brand" style="top:277px">
      <span class="brand__name"><span class="brand__mark"></span>LEDGE CRAFTS</span>
      <span class="brand__tag">FOR ALL TYPES OF PROJECTS</span>
    </div>
    <h1 class="headline">MOULDING FACTORY<br>OUTLET DIRECT SALE</h1>
    <div class="divider"></div>
    <p class="intro">Supply high quality Crown mouldings, baseboards, casings and wainscotings with competitive Price.</p>
    <div class="service">INSTALLATION &amp; DELIVERY</div>
    <div class="collage" role="img" aria-label="Collage of wainscoting panels, baseboard and crown moulding products"></div>
    <p class="contact">416 555 0143, 416 555 0187<br>47 North Willow Vale Rd, Richmond Hill, ON L4B 3K9<br>info@ledgecrafts.example</p>
  </section>

  <section class="hanger hanger--back">
    <svg class="top" width="248" height="320" viewBox="0 0 248 320">
      <defs>
        <linearGradient id="factoryBack" x1="0" y1="0" x2="0" y2="1">
          <stop offset="0" stop-color="#bcc3c6"/>
          <stop offset=".6" stop-color="#7b8789"/>
          <stop offset="1" stop-color="#56625f"/>
        </linearGradient>
      </defs>
      <path d="M0 0H248V312Q124 204 0 312Z" fill="url(#factoryBack)" role="img" aria-label="Photo of a moulding factory workshop"/>
      <path d="M0 314Q124 206 248 314" fill="none" stroke="var(--orange)" stroke-width="4"/>
      <rect x="0" y="66" width="110" height="24" fill="var(--bg)"/>
      <circle cx="125" cy="77" r="51" fill="var(--bg)"/>
    </svg>
    <div class="brand" style="top:295px">
      <span class="brand__name"><span class="brand__mark"></span>LEDGE CRAFTS</span>
      <span class="brand__tag">FOR ALL TYPES OF PROJECTS</span>
    </div>
    <p class="slogan">Convert plain room into<br>designer’s interiors</p>
    <div class="swatch swatch--baseboard" role="img" aria-label="Baseboard and casing detail"></div>
    <div class="swatch swatch--orange swatch--crown" role="img" aria-label="Crown moulding profile"></div>
    <div class="swatch swatch--orange swatch--wainscot" role="img" aria-label="Wainscoting wall panels"></div>
    <div class="swatch swatch--feature" role="img" aria-label="Dark feature wall with geometric panels"></div>
    <p class="contact" style="top:629px">416 555 0143, 416 555 0187<br>47 North Willow Vale Rd, Richmond Hill, ON L4B 3K9<br>info@ledgecrafts.example</p>
  </section>

</main>
</body>
</html>
```